Velora Beauty Clinic

I need a web design for a Cosmetic Surgery Clinic. The current site is velora-beauty-clinic.example. The design should be:
- Flat Design with big banner
- Warm colors
- Responsive Layout
- SEO friendly

Cosmetic

```html
<!DOCTYPE html>
<html lang="en">
<head>
<meta charset="utf-8">
<title>Velora Beauty Clinic – Face, Body, Breast Plastic Surgery</title>
<link rel="stylesheet" href="https://fonts.googleapis.com/css2?family=Mada:wght@300;400;500;600&display=swap">
<style>
:root{
  --red:#e0322e;
  --navy:#27354a;
  --navy-deep:#213044;
  --navy-soft:#3a4c66;
  --ink:#2b3444;
  --muted:#5a6270;
  --paper:#ffffff;
  --panel:#f2f2f2;
  --field:#ffffff;
  --skin-soft:#e6d2c4;
  --skin-mid:#d8b9a4;
  --mist:#dfe3e7;
}
*{box-sizing:border-box;margin:0;padding:0}
html,body{width:1200px;height:2586px;overflow:hidden}
body{font-family:"Mada",sans-serif;color:var(--ink);background:var(--paper);position:relative}
.section{position:absolute;left:0;width:1200px}
.abs{position:absolute}
.btn{position:absolute;display:flex;align-items:center;justify-content:center;color:#fff;font-size:16px;letter-spacing:.3px;text-transform:uppercase}
.btn-navy{background:var(--navy)}
.btn-red{background:var(--red)}

/* header */
.site-header{top:0;height:98px}
.brand{left:74px;top:20px;font-size:31px;line-height:34px;font-weight:400;color:var(--red);width:360px}
.call{right:74px;top:28px}
.call-label{font-size:15px;color:var(--red);font-weight:500}
.call-number{font-size:28px;color:var(--ink);font-weight:500;line-height:32px}

/* nav */
.main-nav{top:98px;height:49px;background:var(--red)}
.main-nav ul{list-style:none;display:flex;position:absolute;left:74px;top:0;height:49px}
.main-nav li{height:49px;display:flex;align-items:center;padding:0 17px;color:#fff;font-size:15px;text-transform:uppercase;margin-right:13px}
.main-nav li.active{background:var(--navy)}

/* hero */
.hero{top:147px;height:470px;background:linear-gradient(90deg,#dfe2e5 0%,#e7e9eb 55%,#d9dcdf 100%)}
.hero-photo{left:603px;top:0;width:597px;height:470px;background:linear-gradient(90deg,var(--mist) 0%,var(--skin-soft) 45%,var(--skin-mid) 100%)}
.hero-title{left:72px;top:104px;font-size:46px;font-weight:500;color:var(--ink);letter-spacing:.5px}
.hero-list{left:74px;top:166px;list-style:none;font-size:33px;line-height:44px;color:var(--red);font-weight:500}
.hero .btn{left:74px;top:331px;width:230px;height:41px;text-transform:none;font-size:17px}
.dots{left:74px;top:385px;display:flex;gap:6px}
.dots span{width:12px;height:12px;border-radius:50%;background:#8c929c}
.dots span.on{background:var(--navy)}

/* intro */
.intro{top:617px;height:174px;text-align:center}
.intro h2{position:absolute;left:0;right:0;top:34px;font-size:25px;font-weight:400;color:var(--red)}
.intro p{position:absolute;left:100px;right:100px;top:78px;font-size:17px;line-height:30px;color:var(--muted)}

/* treatments */
.treatments{top:791px;height:437px;background:var(--navy);color:#fff;text-align:center}
.treatments h2{position:absolute;left:0;right:0;top:40px;font-size:25px;font-weight:400;letter-spacing:.3px}
.treatment{position:absolute;top:112px;width:310px;margin-left:-155px}
.treatment .thumb{width:180px;height:180px;border-radius:50%;margin:0 auto;border:4px solid #fff;background:linear-gradient(135deg,var(--skin-soft),var(--skin-mid))}
.treatment h3{margin-top:30px;font-size:18px;font-weight:500;letter-spacing:.3px}
.treatment p{margin-top:12px;font-size:13px;line-height:24px;color:#d5dae2}

/* experience */
.experience{top:1228px;height:344px}
.experience h2{position:absolute;left:74px;top:36px;font-size:25px;font-weight:400;color:var(--red)}
.experience .copy{left:74px;top:78px;width:425px;font-size:12.5px;line-height:21px;color:var(--muted)}
.experience .copy p+p{margin-top:6px}
.experience .btn{left:74px;top:278px;width:137px;height:38px;font-size:15px}
.doctor-photo{left:510px;top:18px;width:283px;height:326px;background:linear-gradient(180deg,#eef0f2 0%,#c8d6e4 100%)}
.packages{left:793px;top:40px;width:333px;height:276px;background:var(--panel);padding:22px 22px}
.packages h3{font-size:20px;font-weight:400;color:var(--red);line-height:30px}
.packages p{margin-top:10px;font-size:12.5px;line-height:21px;color:var(--muted)}

/* blog */
.blog{top:1572px;height:302px;background:var(--red);color:#fff}
.blog h2{position:absolute;left:74px;top:32px;font-size:25px;font-weight:400}
.blog .rule{left:380px;top:50px;width:670px;height:1px;background:rgba(255,255,255,.35)}
.blog .arrow{top:36px;width:26px;height:26px;border:1px solid rgba(255,255,255,.8);display:flex;align-items:center;justify-content:center}
.blog-photo{left:74px;top:88px;width:293px;height:183px;background:linear-gradient(135deg,#eef0f2 0%,var(--skin-soft) 100%);border:3px solid #f3a39a}
.blog-post{left:403px;top:88px;width:723px}
.blog-post h3{font-size:21px;font-weight:400}
.blog-post time{display:block;margin-top:6px;font-size:13px;color:var(--navy);font-weight:500}
.blog-post p{margin-top:8px;font-size:12.5px;line-height:22px;color:#fde0dc}
.blog .btn{left:403px;top:236px;width:141px;height:37px;font-size:15px}

/* testimonials */
.testimonials{top:1874px;height:286px;text-align:center}
.testimonials h2{position:absolute;left:0;right:0;top:34px;font-size:25px;font-weight:400;color:var(--red)}
.quote-mark{top:92px;font-size:64px;line-height:60px;color:var(--muted);font-weight:600}
.testimonials blockquote{position:absolute;left:138px;right:138px;top:86px;font-size:13.5px;line-height:22px;color:var(--muted)}
.testimonials .name{position:absolute;left:0;right:0;top:152px;font-size:14px;color:var(--ink);font-weight:500}
.testimonials .treatment-type{position:absolute;left:0;right:0;top:176px;font-size:12.5px;color:var(--red)}
.testimonials .btn{left:488px;top:212px;width:224px;height:36px;font-size:15px}

/* contact */
.contact{top:2160px;height:343px;background:var(--navy)}
.contact h2{position:absolute;left:0;right:0;top:28px;text-align:center;font-size:25px;font-weight:400;color:#fff}
.field{position:absolute;background:var(--field);width:331px;height:48px;padding:0 14px;display:flex;align-items:center;font-size:14px;font-style:italic;color:#8a909a;box-shadow:inset 0 -8px 12px rgba(0,0,0,.06)}
.field.message{align-items:flex-start;padding-top:14px;height:166px}
.field b{color:var(--red);font-weight:400}
.contact .btn{left:434px;top:268px;width:331px;height:47px;font-size:17px}
.contact-info{left:817px;top:88px;width:309px;height:227px;background:var(--navy-soft);padding:18px 24px;color:#fff}
.contact-info h3{font-size:19px;font-weight:400}
.contact-info .org{margin-top:12px;font-size:17px}
.contact-info address{font-style:normal;font-size:14px;line-height:24px;color:#d4dae3;margin-top:4px}
.contact-info .line{font-size:13px;line-height:24px;white-space:nowrap}

/* footer */
.site-footer{top:2503px;height:83px;background:var(--navy-deep)}
.site-footer small{position:absolute;left:74px;top:32px;font-size:13px;color:#7f8a99}
.social{position:absolute;right:74px;top:24px;display:flex;gap:8px}
.social span{width:35px;height:35px;border-radius:50%}
</style>
</head>
<body>

<header class="section site-header">
  <div class="abs brand">Velora Beauty Clinic</div>
  <div class="abs call">
    <div class="call-label">Call To Appointment:</div>
    <div class="call-number">555-014-2290</div>
  </div>
</header>

<nav class="section main-nav">
  <ul>
    <li class="active">Home</li>
    <li>About Us</li>
    <li>Our Treatments</li>
    <li>Gallery</li>
    <li>Testimonials</li>
    <li>Blog</li>
    <li>Contact Us</li>
  </ul>
</nav>

<section class="section hero">
  <div class="abs hero-photo" role="img" aria-label="Photo of a body contouring patient marked for surgery"></div>
  <h1 class="abs hero-title">BODY PLASTIC SURGERY</h1>
  <ul class="abs hero-list">
    <li>- Liposuction</li>
    <li>- Tummy Tuck</li>
    <li>- Upper Arm Lift</li>
  </ul>
  <a class="btn btn-red">Cosmetic Surgery Details</a>
  <div class="abs dots"><span class="on"></span><span></span><span></span><span></span></div>
</section>

<section class="section intro">
  <h2>FACE, BODY, BREAST PLASTIC SURGERY</h2>
  <p>Velora Beauty Clinic offers a range of plastic and reconstructive surgery options at affordable prices for those considering medical tourism abroad.</p>
</section>

<section class="section treatments">
  <h2>AESTHETIC PLASTIC SURGERY TREATMENTS</h2>
  <article class="treatment" style="left:240px">
    <div class="thumb" role="img" aria-label="Photo for face plastic surgery"></div>
    <h3>FACE PLASTIC SURGERY</h3>
    <p>Aliquam molestie, mi et imperdiet euismod, dui purus auctor tellus, et interdum lacus lectus et ante</p>
  </article>
  <article class="treatment" style="left:600px">
    <div class="thumb" role="img" aria-label="Photo for breast plastic surgery"></div>
    <h3>BREAST PLASTIC SURGERY</h3>
    <p>Aliquam molestie, mi et imperdiet euismod, dui purus auctor tellus, et interdum lacus lectus et ante</p>
  </article>
  <article class="treatment" style="left:960px">
    <div class="thumb" role="img" aria-label="Photo for body plastic surgery"></div>
    <h3>BODY PLASTIC SURGERY</h3>
    <p>Aliquam molestie, mi et imperdiet euismod, dui purus auctor tellus, et interdum lacus lectus et ante</p>
  </article>
</section>

<section class="section experience">
  <h2>OUR EXPERIENCE SHOWS</h2>
  <div class="abs copy">
    <p>If you are considering cosmetic surgery abroad look no further. Plastic surgery abroad is an opportunity to give a desired area of your body a new and improved look. At Velora Beauty Clinic, we promise to deliver the best plastic surgery options and offer outstanding solutions for you and your body. We want to make sure you look the best that you possibly can without compromise.</p>
    <p>Velora Beauty Clinic specialises in facial, breast and body cosmetic and reconstructive surgeries.</p>
  </div>
  <a class="btn btn-navy">Read More</a>
  <div class="abs doctor-photo" role="img" aria-label="Portrait photo of the clinic's surgeon"></div>
  <aside class="abs packages">
    <h3>COSMETIC SURGERY HOLIDAY PACKAGES IN CYPRUS</h3>
    <p>If you are considering medical tourism, Velora Beauty Clinic can offer you tailor made affordable cosmetic surgery holiday packages in Cyprus including accommodation and travel arrangements that suit your specific needs. We offer you top quality cosmetic surgery procedures abroad at affordable cosmetic surgery prices with dedicated aftercare.</p>
  </aside>
</section>

<section class="section blog">
  <h2>COSMETIC SURGERY BLOG</h2>
  <div class="abs rule"></div>
  <span class="abs arrow" style="left:1070px"><svg width="8" height="12" viewBox="0 0 8 12"><path d="M6 1 1 6l5 5" fill="none" stroke="#fff" stroke-width="1.6"/></svg></span>
  <span class="abs arrow" style="left:1100px"><svg width="8" height="12" viewBox="0 0 8 12"><path d="m2 1 5 5-5 5" fill="none" stroke="#fff" stroke-width="1.6"/></svg></span>
  <div class="abs blog-photo" role="img" aria-label="Photo illustrating a facial cosmetic surgery guide"></div>
  <article class="abs blog-post">
    <h3>A Guide To Cosmetic Surgery in Cyprus</h3>
    <time>17. 11. 2014</time>
    <p>Advantages of cosmetic surgery in Cyprus. You can save money. Cosmetic surgery is not classified as a medical necessity in most healthcare systems, so most people have to pay for their treatment, even if their medical. Suspendisse lobortis turpis in odio blandit ac interdum lorem euismod. Etiam risus massa, vulputate eu pellentesque et, consectetur a neque.</p>
  </article>
  <a class="btn btn-navy">Read More</a>
</section>

<section class="section testimonials">
  <h2>COSMETIC SURGERY TESTIMONIALS</h2>
  <span class="abs quote-mark" style="left:72px">&ldquo;</span>
  <span class="abs quote-mark" style="right:72px">&rdquo;</span>
  <blockquote>I work within health myself and can honestly say Dr Arden impressed me with his polite warming maner, professionalism and amazing competence. I am absolutley over the moon with the results and just regret not getting the procedure done sooner!!</blockquote>
  <div class="name">Marisa</div>
  <div class="treatment-type">Rhinoplasty and Breast Enlargement</div>
  <a class="btn btn-navy">Read All Testimonials</a>
</section>

<section class="section contact">
  <h2>CONTACT US</h2>
  <div class="field" style="left:74px;top:88px">Name<b>*</b></div>
  <div class="field" style="left:74px;top:148px">Email Address<b>*</b></div>
  <div class="field" style="left:74px;top:208px">Phone No.<b>*</b></div>
  <div class="field" style="left:74px;top:267px">Subject<b>*</b></div>
  <div class="field message" style="left:434px;top:88px">Message<b>*</b></div>
  <a class="btn btn-red">Submit Now</a>
  <div class="abs contact-info">
    <h3>CONTACT INFO</h3>
    <div class="org">Velora Beauty Clinic</div>
    <address>14 Linden Row<br>Larnaca, LC6 020</address>
    <div class="line">Ph: 0700 555 0148</div>
    <div class="line">Email: hello@velora-beauty-clinic.example</div>
  </div>
</section>

<footer class="section site-footer">
  <small>© 2015 Velora Beauty Clinic. All Right Reserved</small>
  <div class="social">
    <span style="background:#3b5a98"></span>
    <span style="background:#2aa3d6"></span>
    <span style="background:#c4302b"></span>
  </div>
</footer>

</body>
</html>
```